TELVORIQ HOA Portal Site for Public

Clean up and organize current website; need website to look good and functional; this is a HOA (homeowner association management) website where homeowners can login and pay their bill, general information about a HOA, monthly newsletter page.
Competitors:
https://plumbrivet.com/
https://duskorrahill.com/
https://www.qxlivingspan.com/nevada
http://www.bpt-hoa.com/

Target Market(s)

homeowners

Industry/Entity Type

Real Estate

Coding

Coded - Design and coding required

Number of Pages Required

5+ page

Font styles to use
Serif

Colors
0292cd
33a6d7
e667a6
e34297

Requirements
Must have
• login to pay
• services page
• contact us
• order resale package
Nice to have
• page why an HOA would contract us

```html
<!DOCTYPE html>
<html lang="en">
<head>
<meta charset="utf-8">
<title>TELVORIQ HOA</title>
<link href="https://fonts.googleapis.com/css2?family=Cinzel:wght@700&family=Lato:wght@400&display=swap" rel="stylesheet">
<style>
:root{
  --blue-dark:#0292cd;
  --blue-light:#33a6d7;
  --pink-light:#e667a6;
  --pink-dark:#e34297;
  --ink:#111111;
  --text:#555555;
  --white:#ffffff;
  --line:#cfcfcf;
  --serif:'Cinzel', 'Times New Roman', serif;
  --sans:'Lato', Arial, sans-serif;
}
*{margin:0;padding:0;box-sizing:border-box}
html,body{width:1200px;height:2760px;overflow:hidden}
body{position:relative;font-family:var(--sans);color:var(--text);background:var(--white)}
.abs{position:absolute}

.hero{left:0;top:0;width:1200px;height:646px;background:linear-gradient(180deg,#3a3a3a 0%,#4a4a4a 45%,#2e2e2e 100%)}
.hero-photo{position:absolute;inset:0;background:radial-gradient(ellipse at 30% 40%,#5a5a5a 0%,transparent 60%),radial-gradient(ellipse at 80% 60%,#444 0%,transparent 55%)}
.brand{left:80px;top:28px;font-family:var(--serif);font-size:29px;color:var(--white);letter-spacing:.5px}
.nav{top:38px;right:79px;display:flex;gap:27px;font-size:14px;color:var(--white);text-transform:uppercase}
.nav a{color:inherit;text-decoration:none;position:relative}
.nav a.active::before{content:"";position:absolute;left:0;top:-9px;width:16px;height:1px;background:var(--white)}
.hero-title{left:0;width:1200px;top:262px;text-align:center;font-family:var(--serif);font-size:38px;color:var(--white);letter-spacing:.5px}
.hero-text{left:260px;width:680px;top:336px;text-align:center;font-size:18px;line-height:32px;color:var(--white)}

.bill-band{left:0;top:646px;width:1200px;height:156px;background:linear-gradient(180deg,var(--blue-light),var(--blue-dark))}
.bill-title{left:80px;top:683px;font-family:var(--serif);font-size:31px;color:var(--white)}
.bill-text{left:79px;top:733px;font-size:18px;color:var(--white)}
.pill{border-radius:26px;background:linear-gradient(180deg,var(--pink-light),var(--pink-dark));color:var(--white);font-family:var(--serif);text-align:center}
.login-btn{left:967px;top:698px;width:156px;height:51px;line-height:51px;font-size:19px}

.section-title{left:0;width:1200px;text-align:center;font-family:var(--serif);font-size:35px;color:var(--ink)}
.section-lead{left:260px;width:680px;text-align:center;font-size:14px;line-height:25px}
.photo{background:linear-gradient(135deg,#c9a98a,#6f7f93)}
.photo-house{background:linear-gradient(180deg,#a9b6c8 0%,#b67f63 35%,#9c6a5a 70%,#6b6a55 100%)}
.card-title{text-align:center;font-size:19px;line-height:29px;color:#333}
.card-text{text-align:center;font-size:14px;line-height:25px}

.offer{left:0;top:1531px;width:1200px;height:479px;background:var(--ink)}
.offer-photo{left:0;top:1531px;width:562px;height:479px;background:linear-gradient(135deg,#e6e6e6 0%,#8ea2bf 45%,#5c7a4a 100%)}
.offer-title{left:652px;top:1610px;font-family:var(--serif);font-size:32px;color:var(--white)}
.offer-list{left:652px;top:1672px;width:480px;list-style:none;font-size:14px;line-height:25px;color:var(--white)}
.offer-list li{margin-bottom:14px}
.read-more{left:655px;top:1903px;font-family:var(--serif);font-size:14px;color:var(--white);text-decoration:underline;display:flex;align-items:center;gap:16px}

.field{border:1px solid var(--line);font-size:14px;color:#777;padding:14px 17px;background:var(--white)}
.submit-btn{left:522px;top:2456px;width:156px;height:51px;line-height:51px;font-size:19px}

.footer{left:0;top:2583px;width:1200px;height:177px;background:var(--ink)}
.footer-nav{left:0;width:1200px;top:2638px;text-align:center;font-size:15px;color:var(--white)}
.footer-nav span.sep{margin:0 22px}
.copyright{left:0;width:1200px;top:2690px;text-align:center;font-size:14px;color:var(--white)}
</style>
</head>
<body>

<header class="abs hero">
  <div class="hero-photo" role="img" aria-label="Darkened photo of a Mediterranean home behind palm trees and a gate"></div>
</header>
<div class="abs brand">TELVORIQ HOA</div>
<nav class="abs nav">
  <a class="active" href="#">Home</a>
  <a href="#">Services</a>
  <a href="#">Order Resale Package</a>
  <a href="#">Why an HAO would contract us</a>
  <a href="#">Contact</a>
</nav>
<h1 class="abs hero-title">LOREM IPSUM IS SIMPLY DUMMY.</h1>
<p class="abs hero-text">Lorem ipsum dolor sit amet, consectetur adipiscing elit, sed do eiusmod tempor incididunt ut labore et dolore magna aliqua. Ut enim ad minim vm, quis.</p>

<section class="abs bill-band"></section>
<h2 class="abs bill-title">LOGIN TO PAY YOUR BILLS</h2>
<p class="abs bill-text">homeowners can login and pay their bill</p>
<a class="abs pill login-btn">LOGIN</a>

<h2 class="abs section-title" style="top:848px">OUR SERVICES</h2>
<p class="abs section-lead" style="top:909px">Lorem ipsum dolor sit amet, consectetur adipiscing elit, sed do eiusmod tempor incididunt ut labore et dolore magna aliqua. Ut enim ad minim vm, quis nostrud exercitation ullamco laboris nisi ut.</p>

<div class="abs photo" style="left:77px;top:1016px;width:500px;height:301px" role="img" aria-label="Photo of a couple reviewing documents with an advisor"></div>
<div class="abs photo photo-house" style="left:623px;top:1016px;width:500px;height:301px" role="img" aria-label="Photo of a tiled-roof stucco home with desert mountains behind"></div>

<h3 class="abs card-title" style="left:77px;width:500px;top:1345px">Association Management Services</h3>
<p class="abs card-text" style="left:87px;width:480px;top:1387px">Lorem ipsum dolor sit amet, consectetur adipiscing elit, sed do eiusmod tempor incididunt ut labore et dolore magna aliqua. Ut enim ad minim vm, quis nostrud exercitation ullamco laboris nisi ut.</p>
<h3 class="abs card-title" style="left:673px;width:400px;top:1345px">TELVOR manages communities throughout Southern Nevada</h3>
<p class="abs card-text" style="left:633px;width:480px;top:1412px">Lorem ipsum dolor sit amet, consectetur adipiscing elit, sed do eiusmod tempor incididunt ut labore et dolore magna aliqua. Ut enim ad.</p>

<section class="abs offer"></section>
<div class="abs offer-photo" role="img" aria-label="Photo of two colleagues looking at a tablet in an office"></div>
<h2 class="abs offer-title">WHAT WE OFFER</h2>
<ul class="abs offer-list">
  <li>Accessible, licensed Association Managers</li>
  <li>24 hour Web site access: online account information</li>
  <li>24 hour emergency service</li>
  <li>Provide monthly financial reports to the Board of Directors</li>
  <li>Read, study and understand all governing documents of the Association. Correspond with members in violation of the CC&amp;Rs, By-laws...</li>
</ul>
<a class="abs read-more">READ MORE
  <svg width="27" height="12" viewBox="0 0 27 12"><path d="M0 6H25M20 1L25.5 6L20 11" fill="none" stroke="#fff" stroke-width="1.6"/></svg>
</a>

<h2 class="abs section-title" style="top:2056px">GET IN TOUCH</h2>
<p class="abs section-lead" style="top:2117px">Lorem ipsum dolor sit amet, consectetur adipiscing elit, sed do eiusmod tempor incididunt ut labore et dolore magna aliqua. Ut enim ad minim vm, quis nostrud exercitation ullamco laboris nisi ut.</p>

<form>
  <div class="abs field" style="left:236px;top:2212px;width:354px;height:47px">Name</div>
  <div class="abs field" style="left:611px;top:2212px;width:354px;height:47px">Phone</div>
  <div class="abs field" style="left:236px;top:2275px;width:354px;height:47px">Email</div>
  <div class="abs field" style="left:611px;top:2275px;width:354px;height:47px">Subject</div>
  <div class="abs field" style="left:236px;top:2337px;width:729px;height:104px">Message</div>
  <a class="abs pill submit-btn">SUBMIT</a>
</form>

<footer class="abs footer"></footer>
<nav class="abs footer-nav">Home<span class="sep">|</span>Services We Provide<span class="sep">|</span>Order resale package<span class="sep">|</span>Why an HOA would contract us<span class="sep">|</span>Contact</nav>
<p class="abs copyright">©TELVORIQ HOA- 2019. All Rights Reserved.</p>

</body>
</html>
```